Build a website for a print shop

My client operates a family-owned print shop business and would like to have a website for his business. The name of the business is Lorn's Print Shop. I am posting here 2 files: one is just a sign that he has on his shop, and the second one is a picture of his grandfather who started this business several years ago. You can decide if you want to use these pictures in your design, or not- it is not mandatory. A few notes:
1- Please do not copy designs from other sites, such as layoutbarn
2- If you see pirated designs from other designers, please let me know in private chat
3- The final deliverable is:
a) Two working HTML pages, one for home page, and another for other pages
b) All graphics used
4- If you actually create the demo pages as part of your proposal, the client will have a much easier time to decide, as they are not computer-savvy

Thanks and happy bidding!

**NOTE: PLEASE SEE CLARIFICATION BOARD FOR FURTHER INFO

```html
<!DOCTYPE html>
<html lang="en">
<head>
<meta charset="utf-8">
<title>Lorn's Print Shop</title>
<link href="https://fonts.googleapis.com/css2?family=Mulish:ital,wght@0,400;0,600;0,700;0,800;0,900;1,400&display=swap" rel="stylesheet">
<style>
:root{
  --red:#d9261c;
  --navy:#2a2170;
  --taupe:#7a7166;
  --text:#555;
  --muted:#8a8a8a;
  --line:#ececec;
  --pink:#fccfd8;
  --yellow:#f7e136;
  --cyan:#9ae9f0;
  --white:#fff;
}
*{margin:0;padding:0;box-sizing:border-box}
html,body{width:1200px;height:3107px;overflow:hidden;background:var(--white)}
body{position:relative;font-family:'Mulish',sans-serif;color:var(--text)}
.abs{position:absolute}
/* header */
.site-header{left:0;top:0;width:1200px;height:86px;background:var(--white)}
.brand{left:112px;top:20px;display:flex;align-items:center;gap:12px}
.brand-mark{width:30px;height:30px;background:var(--red)}
.brand-name{font-size:24px;font-weight:700;color:var(--red)}
.main-nav{left:500px;top:34px;display:flex;gap:0;font-size:13px;color:#444}
.main-nav a{display:block;padding:0 14px;text-decoration:none;color:inherit;height:34px}
.main-nav a.active{color:var(--red);border-bottom:2px solid var(--red)}
.nav-sep{left:940px;top:24px;width:1px;height:38px;background:var(--line)}
.social{display:flex;gap:6px}
.social span{width:25px;height:25px;border-radius:50%;background:#b5b5b5;display:block}
.social span.accent{background:#35b8ea}
.header-social{left:968px;top:31px}
/* hero */
.hero{left:0;top:86px;width:1200px;height:465px;background:linear-gradient(120deg,#6f6658 0%,#8a806f 45%,#5e564a 100%)}
.hero-title{left:112px;top:220px;font-size:53px;font-weight:900;color:var(--white);letter-spacing:-0.5px}
.dash{height:4px;background:var(--white);border-radius:2px}
.hero-text{left:112px;top:324px;width:460px;font-size:12.5px;line-height:21px;color:#f3f0ea}
.btn{display:flex;align-items:center;justify-content:center;background:var(--red);color:var(--white);font-weight:700;border-radius:20px;box-shadow:0 3px 0 #8c1710;text-transform:uppercase}
.hero-btn{left:112px;top:411px;width:133px;height:36px;font-size:12.5px}
.dots{left:1080px;top:410px;display:flex;flex-direction:column;gap:10px}
.dots span{width:6px;height:19px;border-radius:3px;background:var(--white)}
.dots span.on{background:var(--white);border:2px solid var(--red)}
/* features */
.feature-wrap{left:112px;top:536px;width:976px;height:204px;background:var(--white);box-shadow:0 2px 8px rgba(0,0,0,.15)}
.feature{top:555px;width:300px;height:166px;display:flex;align-items:center;padding-left:20px;gap:14px}
.feature svg{flex:none}
.feature-title{font-size:18px;font-weight:700;color:var(--navy);line-height:19px;text-align:center}
.feature-link{margin-top:10px;font-size:13px;font-weight:700;color:var(--red);text-align:center}
.pink{background:var(--pink)}.yellow{background:var(--yellow)}.cyan{background:var(--cyan)}
.rule{left:0;width:1200px;height:1px;background:var(--line)}
/* about */
.eyebrow{left:112px;top:881px;font-size:18px;color:#555}
.about-title{left:112px;top:914px;font-size:24.5px;font-weight:700;color:var(--navy);line-height:31px}
.about-text{left:112px;top:1004px;width:445px;font-size:11px;font-style:italic;line-height:21px;color:#777}
.about-btn{left:112px;top:1114px;width:115px;height:29px;font-size:11px}
.about-shadow{left:611px;top:876px;width:461px;height:293px;background:#7d776f}
.about-photo{left:626px;top:864px;width:462px;height:290px;background:linear-gradient(135deg,#c8c3bc,#6e6a66 55%,#3b4b5c)}
/* services */
.services{left:0;top:1228px;width:1200px;height:449px;background:var(--taupe)}
.section-title{width:1200px;left:0;text-align:center;font-size:30px;font-weight:600}
.section-sub{width:1200px;left:0;text-align:center;font-size:11px;font-style:italic}
.service{top:1395px;width:230px;text-align:center;color:var(--white)}
.service h3{margin-top:14px;font-size:14.5px;font-weight:600;text-transform:uppercase}
.service p{margin-top:8px;font-size:11px;line-height:19px;color:#f1ede7}
.service .more{margin-top:10px;font-size:12.5px;font-weight:700}
.service .more b{color:var(--red);font-weight:400}
/* portfolio */
.tile{background:linear-gradient(135deg,#8a7a6d,#c03224 55%,#3b3b3b)}
.tile.print{background:linear-gradient(135deg,#d8d8d8,#8f9aa6 50%,#c9a04d)}
.tile.roll{background:linear-gradient(160deg,#2a2a2a,#d62418 45%,#7a0f0a)}
.tile.hands{background:linear-gradient(135deg,#a78c6c,#c9322a 50%,#e6e1d8)}
.tile.shop{background:linear-gradient(160deg,#cfd3d6,#7b8792 50%,#e4e6e8)}
.tile.overlay{background:#2b2b2b;border:3px solid var(--red);color:var(--white);display:flex;flex-direction:column;align-items:center;justify-content:center;gap:8px;font-size:15px;font-weight:600}
.view-btn{left:440px;top:2333px;width:320px;height:37px;font-size:14.5px;font-weight:600}
/* testimonials */
.quote-card{left:236px;top:2597px;width:726px;height:163px;border:1px solid #e3e3e3;border-radius:26px;box-shadow:0 2px 6px rgba(0,0,0,.05);text-align:center}
.quote-card h4{margin-top:20px;font-size:17.5px;font-weight:600;color:#555}
.quote-card p{margin:10px auto 0;width:610px;font-size:12.5px;font-style:italic;line-height:21px;color:#a5a5a5}
.quote-mark{left:290px;top:2620px;font-size:42px;font-weight:900;color:#ddd;font-style:italic}
.arrow{top:2661px;width:35px;height:35px;border-radius:50%;display:flex;align-items:center;justify-content:center;font-size:18px}
.avatar{left:561px;top:2724px;width:72px;height:72px;border-radius:50%;border:3px solid #9ab0d6;background:linear-gradient(#c6d1e0,#34465e)}
.client{left:0;width:1200px;text-align:center}
/* footer */
.site-footer{left:0;top:2907px;width:1200px;height:200px;background:var(--taupe);color:var(--white)}
.f-label{font-size:9px}
.f-value{font-size:21px}
.f-small{font-size:9px}
.footer-social span{width:28px;height:28px;background:#3b3632}
.footer-social span.accent{background:#35b8ea}
</style>
</head>
<body>

<header class="site-header abs">
  <div class="brand abs"><span class="brand-mark"></span><span class="brand-name">Lorn's Print Shop</span></div>
  <nav class="main-nav abs">
    <a class="active">Home</a><a>About</a><a>Services</a><a>Portfolio</a><a>Blog</a><a>Contact</a>
  </nav>
  <div class="nav-sep abs"></div>
  <div class="social header-social abs"><span></span><span class="accent"></span><span></span><span></span></div>
</header>

<section class="hero abs" role="img" aria-label="Sepia photo of an elderly printer working at a vintage printing press"></section>
<h1 class="hero-title abs">LORN'S PRINT SHOP</h1>
<div class="dash abs" style="left:112px;top:297px;width:83px"></div>
<div class="dash abs" style="left:203px;top:297px;width:15px"></div>
<p class="hero-text abs">Lorem ipsum dolor sit amet consectetur adipiscing sed eiusmod tempor incididunt ut labore et dolore magna aliqua Ut enim ad minim veniam nostrud exercitation ullamco laboris.</p>
<div class="btn hero-btn abs">Read More</div>
<div class="dots abs"><span class="on"></span><span></span><span></span></div>

<div class="feature-wrap abs"></div>
<div class="feature pink abs" style="left:131px">
  <svg width="118" height="118" viewBox="0 0 118 118" fill="none" stroke="#6e6760" stroke-width="7" stroke-linejoin="round"><path d="M34 38V10h50v28"/><rect x="6" y="38" width="106" height="48" rx="8"/><rect x="26" y="62" width="66" height="50"/><path d="M38 76h42M38 90h42"/><circle cx="94" cy="52" r="3" fill="#6e6760"/></svg>
  <div><div class="feature-title">LOREM<br>IPSUM DOLOR</div><div class="feature-link">Read More →</div></div>
</div>
<div class="feature yellow abs" style="left:451px">
  <svg width="118" height="118" viewBox="0 0 118 118" fill="none" stroke="#6e6760" stroke-width="7" stroke-linejoin="round"><path d="M34 38V10h50v28"/><rect x="6" y="38" width="106" height="48" rx="8"/><rect x="26" y="62" width="66" height="50"/><path d="M38 76h42M38 90h42"/><circle cx="94" cy="52" r="3" fill="#6e6760"/></svg>
  <div><div class="feature-title">LOREM<br>IPSUM DOLOR</div><div class="feature-link">Read More →</div></div>
</div>
<div class="feature cyan abs" style="left:769px">
  <svg width="118" height="118" viewBox="0 0 118 118" fill="none" stroke="#6e6760" stroke-width="7" stroke-linejoin="round"><path d="M34 38V10h50v28"/><rect x="6" y="38" width="106" height="48" rx="8"/><rect x="26" y="62" width="66" height="50"/><path d="M38 76h42M38 90h42"/><circle cx="94" cy="52" r="3" fill="#6e6760"/></svg>
  <div><div class="feature-title">LOREM<br>IPSUM DOLOR</div><div class="feature-link">Read More →</div></div>
</div>

<div class="rule abs" style="top:803px"></div>

<div class="eyebrow abs">ABOUT US</div>
<h2 class="about-title abs">LOREM IPSUM DOLOR SIT AMET<br>CONSECTETUR ADIPISCING ELIT SED</h2>
<p class="about-text abs">Lorem ipsum dolor sit amet, consectetur adipiscing elit, sed do eiusmod tempor incididunt ut labore et dolore magna aliqua. enim ad minim veniam, quis nostrud exercitation ullamco laboris nisi ut aliquip ex ea commodo consequat. Duis aute irure dolor in...</p>
<div class="btn about-btn abs">Read More</div>
<div class="about-shadow abs"></div>
<div class="about-photo abs" role="img" aria-label="Photo of a man inspecting prints at a large-format printer in a print workshop"></div>

<section class="services abs"></section>
<h2 class="section-title abs" style="top:1280px;color:var(--white)">SERVICES</h2>
<div class="dash abs" style="left:573px;top:1327px;width:31px;height:3px"></div>
<div class="dash abs" style="left:617px;top:1327px;width:10px;height:3px"></div>
<p class="section-sub abs" style="top:1342px;color:#f1ede7">Lorem ipsum dolor sit amet consectetur adipiscing elit sed do eiusmod..</p>

<div class="service abs" style="left:110px">
  <svg width="100" height="100" viewBox="0 0 100 100"><g fill="#fff"><circle cx="50" cy="50" r="38"/><circle cx="50" cy="16" r="16"/><circle cx="50" cy="84" r="16"/><circle cx="16" cy="50" r="16"/><circle cx="84" cy="50" r="16"/><circle cx="26" cy="26" r="16"/><circle cx="74" cy="26" r="16"/><circle cx="26" cy="74" r="16"/><circle cx="74" cy="74" r="16"/></g><g fill="#d9261c"><rect x="38" y="30" width="24" height="10"/><rect x="28" y="42" width="44" height="20" rx="3"/><rect x="37" y="56" width="26" height="16" fill="#fff" stroke="#d9261c" stroke-width="3"/></g></svg>
  <h3>Lorem Ipsum</h3><p>lorem ipsum dolor sit amet consectetur adipiscing elit sed do eiusmod tempor incididunt ut labore et dolore.</p><div class="more">Read More <b>→</b></div>
</div>
<div class="service abs" style="left:360px">
  <svg width="100" height="100" viewBox="0 0 100 100"><g fill="#fff"><circle cx="50" cy="50" r="38"/><circle cx="50" cy="16" r="16"/><circle cx="50" cy="84" r="16"/><circle cx="16" cy="50" r="16"/><circle cx="84" cy="50" r="16"/><circle cx="26" cy="26" r="16"/><circle cx="74" cy="26" r="16"/><circle cx="26" cy="74" r="16"/><circle cx="74" cy="74" r="16"/></g><g fill="#d9261c"><rect x="38" y="30" width="24" height="10"/><rect x="28" y="42" width="44" height="20" rx="3"/><rect x="37" y="56" width="26" height="16" fill="#fff" stroke="#d9261c" stroke-width="3"/></g></svg>
  <h3>Lorem Ipsum</h3><p>lorem ipsum dolor sit amet consectetur adipiscing elit sed do eiusmod tempor incididunt ut labore et dolore.</p><div class="more">Read More <b>→</b></div>
</div>
<div class="service abs" style="left:610px">
  <svg width="100" height="100" viewBox="0 0 100 100"><g fill="#fff"><circle cx="50" cy="50" r="38"/><circle cx="50" cy="16" r="16"/><circle cx="50" cy="84" r="16"/><circle cx="16" cy="50" r="16"/><circle cx="84" cy="50" r="16"/><circle cx="26" cy="26" r="16"/><circle cx="74" cy="26" r="16"/><circle cx="26" cy="74" r="16"/><circle cx="74" cy="74" r="16"/></g><g fill="#d9261c"><rect x="38" y="30" width="24" height="10"/><rect x="28" y="42" width="44" height="20" rx="3"/><rect x="37" y="56" width="26" height="16" fill="#fff" stroke="#d9261c" stroke-width="3"/></g></svg>
  <h3>Lorem Ipsum</h3><p>lorem ipsum dolor sit amet consectetur adipiscing elit sed do eiusmod tempor incididunt ut labore et dolore.</p><div class="more">Read More <b>→</b></div>
</div>
<div class="service abs" style="left:860px">
  <svg width="100" height="100" viewBox="0 0 100 100"><g fill="#fff"><circle cx="50" cy="50" r="38"/><circle cx="50" cy="16" r="16"/><circle cx="50" cy="84" r="16"/><circle cx="16" cy="50" r="16"/><circle cx="84" cy="50" r="16"/><circle cx="26" cy="26" r="16"/><circle cx="74" cy="26" r="16"/><circle cx="26" cy="74" r="16"/><circle cx="74" cy="74" r="16"/></g><g fill="#d9261c"><rect x="38" y="30" width="24" height="10"/><rect x="28" y="42" width="44" height="20" rx="3"/><rect x="37" y="56" width="26" height="16" fill="#fff" stroke="#d9261c" stroke-width="3"/></g></svg>
  <h3>Lorem Ipsum</h3><p>lorem ipsum dolor sit amet consectetur adipiscing elit sed do eiusmod tempor incididunt ut labore et dolore.</p><div class="more">Read More <b>→</b></div>
</div>

<h2 class="section-title abs" style="top:1728px;color:#555">PORTFOLIO</h2>
<div class="dash abs" style="left:573px;top:1775px;width:31px;height:3px;background:#555"></div>
<div class="dash abs" style="left:617px;top:1775px;width:10px;height:3px;background:#555"></div>
<p class="section-sub abs" style="top:1790px;color:#777">Lorem ipsum dolor sit amet consectetur adipiscing elit sed do eiusmod..</p>

<div class="tile hands abs" style="left:112px;top:1840px;width:388px;height:302px" role="img" aria-label="Hands pulling red ink across a screen printing frame"></div>
<div class="tile overlay abs" style="left:503px;top:1840px;width:192px;height:150px">LOREM IPSUM
  <svg width="26" height="26" viewBox="0 0 26 26" fill="none" stroke="#fff" stroke-width="2"><circle cx="11" cy="11" r="8"/><path d="M17 17l7 7M11 7v8M7 11h8"/></svg></div>
<div class="tile print abs" style="left:699px;top:1840px;width:194px;height:150px" role="img" aria-label="Large-format printer outputting colourful posters"></div>
<div class="tile roll abs" style="left:896px;top:1840px;width:192px;height:150px" role="img" aria-label="Red ink rollers on an offset press"></div>
<div class="tile shop abs" style="left:503px;top:1993px;width:390px;height:303px" role="img" aria-label="Print workers examining a large printed sheet on the shop floor"></div>
<div class="tile roll abs" style="left:896px;top:1993px;width:192px;height:150px;background:linear-gradient(135deg,#e5e5e5,#3a2d5a 50%,#d2532a)" role="img" aria-label="Printer head running over a vivid printed banner"></div>
<div class="tile roll abs" style="left:112px;top:2146px;width:193px;height:150px" role="img" aria-label="Red ink rollers on an offset press"></div>
<div class="tile print abs" style="left:308px;top:2146px;width:192px;height:150px" role="img" aria-label="Large-format printer outputting colourful posters"></div>
<div class="tile hands abs" style="left:896px;top:2146px;width:192px;height:150px" role="img" aria-label="Hands pulling red ink across a screen printing frame"></div>

<div class="btn view-btn abs">View More</div>

<div class="rule abs" style="top:2431px"></div>

<h2 class="section-title abs" style="top:2483px;color:#555">TESTIMONIALS</h2>
<div class="dash abs" style="left:573px;top:2530px;width:31px;height:3px;background:#555"></div>
<div class="dash abs" style="left:617px;top:2530px;width:10px;height:3px;background:#555"></div>
<p class="section-sub abs" style="top:2545px;color:#777">Lorem ipsum dolor sit amet consectetur adipiscing elit sed do eiusmod..</p>

<div class="arrow abs" style="left:205px;background:var(--red);color:#fff">‹</div>
<div class="arrow abs" style="left:960px;background:#e6e6e6;color:#555">›</div>
<div class="quote-card abs">
  <h4>Lorem ipsum dolor sit amet consectetur...</h4>
  <p>Lorem ipsum dolor sit amet, consectetur adipiscing elit, sed do eiusmod tempor incididunt dolore magna aliqua. Ut enim ad minim veniam, quis nostrud exercitation ullamco nisi &nbsp;ex ea commodo consequat.</p>
</div>
<div class="quote-mark abs">“</div>
<div class="avatar abs" role="img" aria-label="Portrait of the client"></div>
<div class="client abs" style="top:2808px;font-size:18px;color:#444">Mr Alan P</div>
<div class="client abs" style="top:2832px;font-size:12.5px;font-weight:700;color:#f0a020">June 2018</div>

<footer class="site-footer abs">
  <div class="f-label abs" style="left:112px;top:56px">Toll Free</div>
  <div class="f-value abs" style="left:112px;top:72px">+100-5550-0123</div>
  <div class="f-label abs" style="left:500px;top:56px">Email</div>
  <div class="f-value abs" style="left:500px;top:72px">hello@lornsprintshop.com</div>
  <div class="social footer-social abs" style="left:946px;top:76px"><span></span><span class="accent"></span><span></span><span></span></div>
  <div class="f-small abs" style="left:112px;top:128px">Address : Lorem ipsum dolor sit amet consectetur adipiscing</div>
  <div class="f-small abs" style="left:906px;top:128px">© 2018 lornsprintshop.All rights reserved.</div>
</footer>

</body>
</html>
```